Veterinary Clinic Letterhead - Ridgeview Veterinary Surgery

We need a letterhead design for an established Veterinary Clinic in Kallora called Ridgeview Veterinary Surgery. We are a moderate sized mixed animal veterinary clinic offering a wide variety of veterinary services. The design should use the same colour pattern as those in the logos supplied. The design should also include our address (48 Tulloch Road, Kallora, Northvale, 4891), phone number (07 4158 6734), email (admin@ridgeviewvets.com.au), website (www.ridgeviewvets.com.au) and our opening hours (8am to 5pm Monday to Friday and 8am to 12pm Saturday).
Target Market(s)
Pet owners
Industry/Entity Type
Veterinary
Requirements
Must have
- The logo or modification of it, business address, opening hours, website, phone number and email address

```html
<!DOCTYPE html>
<html lang="en">
<head>
<meta charset="utf-8">
<title>Ridgeview Veterinary Surgery – Letterhead</title>
<link href="https://fonts.googleapis.com/css2?family=Montserrat:wght@400;500;700&family=Roboto:wght@400&display=swap" rel="stylesheet">
<style>
  :root {
    --navy: #0d2b50;
    --ink: #2a2a2a;
    --paper: #ffffff;
    --backdrop: #e4e5e7;
    --swoosh-light: #d9dadc;
    --swoosh-dark: #8c8d90;
    --signature-fill: #e9e9eb;
  }
  * { margin: 0; padding: 0; box-sizing: border-box; }
  html, body { width: 1200px; height: 874px; overflow: hidden; }
  body {
    background: var(--backdrop);
    font-family: "Montserrat", Arial, sans-serif;
    color: var(--ink);
    position: relative;
  }
  .letterhead {
    position: absolute;
    left: 303px; top: 17px;
    width: 594px; height: 840px;
    background: var(--paper);
    overflow: hidden;
    box-shadow: 0 2px 10px rgba(0,0,0,.12);
  }
  .brand {
    position: absolute; left: 48px; top: 52px;
    display: flex; align-items: center; gap: 12px;
  }
  .brand-dot {
    width: 46px; height: 46px; border-radius: 50%;
    background: var(--navy);
  }
  .brand-name {
    font-family: "Montserrat", Arial, sans-serif;
    font-weight: 700; font-size: 15px; line-height: 1.15;
    color: var(--navy); text-transform: uppercase; letter-spacing: .3px;
    width: 170px;
  }
  .contact {
    position: absolute; right: 44px; top: 48px;
    font-family: "Roboto", Arial, sans-serif;
    font-size: 9.5px; line-height: 1.45; text-align: right;
    list-style: none; color: var(--ink);
  }
  .contact li { display: flex; justify-content: flex-end; align-items: center; gap: 5px; }
  .contact svg { width: 8px; height: 8px; fill: var(--navy); }
  .contact .no-icon { padding-right: 13px; }
  .letter {
    position: absolute; left: 70px; top: 168px; width: 452px;
    font-size: 9.6px; line-height: 1.5;
  }
  .recipient { margin-bottom: 2px; }
  .letter p { margin-bottom: 18px; }
  .closing { margin-top: -4px; }
  .signature {
    display: block; width: 110px; height: 44px; margin-top: 10px;
    background: var(--signature-fill); border-radius: 4px;
  }
  .wave { position: absolute; left: 0; top: 0; width: 594px; height: 840px; }
  .hours {
    position: absolute; right: 20px; top: 600px; width: 140px;
    font-family: "Roboto", Arial, sans-serif;
    color: #fff; font-size: 12.5px; line-height: 1.3; text-align: center;
  }
</style>
</head>
<body>
  <main class="letterhead">
    <svg class="wave" viewBox="0 0 594 840" aria-hidden="true">
      <defs>
        <linearGradient id="swoosh" x1="0" y1="1" x2="1" y2="0">
          <stop offset="0" stop-color="var(--swoosh-dark)"/>
          <stop offset="1" stop-color="var(--swoosh-light)"/>
        </linearGradient>
      </defs>
      <path d="M196 840 C320 828 392 770 428 650 C462 540 510 488 594 456 L594 470 C522 500 482 548 448 650 C410 770 342 830 232 840 Z" fill="url(#swoosh)"/>
      <path d="M232 840 C342 830 410 770 448 650 C482 548 522 500 594 470 L594 840 Z" fill="var(--navy)"/>
    </svg>

    <header class="brand">
      <span class="brand-dot"></span>
      <span class="brand-name">Ridgeview Veterinary Surgery</span>
    </header>

    <ul class="contact">
      <li class="no-icon">48 Tulloch Road, Kallora</li>
      <li class="no-icon">Northvale, 4891</li>
      <li>07 4158 6734 <svg viewBox="0 0 10 10"><path d="M2 0.5 L4 2.5 L3 3.6 C3.7 5 5 6.3 6.4 7 L7.5 6 L9.5 8 L8 9.5 C4 9.2 0.8 6 0.5 2 Z"/></svg></li>
      <li>admin@ridgeviewvets.com.au <svg viewBox="0 0 10 10"><path d="M0.5 2 H9.5 V8 H0.5 Z M0.5 2 L5 5.5 L9.5 2" stroke="#fff" stroke-width=".8"/></svg></li>
      <li>www.ridgeviewvets.com.au <svg viewBox="0 0 10 10"><circle cx="5" cy="5" r="4.5"/></svg></li>
    </ul>

    <section class="letter">
      <div class="recipient">
        Mr/s<br>First Name and Last Name<br>Company Name<br>Address
      </div>
      <p>Lorem Ipsum is simply dummy text of the printing and typesetting industry. Lorem Ipsum has been the industry's standard dummy text ever since the 1500s, when an unknown printer took a galley of type and scrambled it to make a type specimen book. It has survived not only five centuries, but also the leap into electronic typesetting, remaining essentially unchanged. It was popularised in the 1960s.</p>
      <p>he standard chunk of Lorem Ipsum used since the 1500s is reproduced below for those interested. Sections 1.10.32 and 1.10.33 from "de Finibus Bonorum et Malorum" by Aurelian Vost are also reproduced in their exact original form, accompanied by English versions from the 1914 translation by H. Marlow. Lorem ipsum dolor sit amet, consectetur adipiscing elit, sed do eiusmod tempor incididunt ut labore et dolore magna aliqua.</p>
      <p>It is a long established fact that a reader will be distracted by the readable content of a page when looking at its layout. The point of using Lorem Ipsum is that it has a more-or-less normal distribution of letters, as opposed to using 'Content here, content here', making it look like readable English. Many desktop publishing packages and web page editors now .</p>
      <div class="closing">Your Sincerely,</div>
      <span class="signature" role="img" aria-label="Handwritten signature"></span>
    </section>

    <div class="hours">8am to 5pm<br>Monday to Friday<br>and<br>8am to 12pm<br>Saturday</div>
  </main>
</body>
</html>
```